Broschüre für Gleichstellungsstelle einer kommunalen Stadtverwaltung
Zielgruppe
Wir sind die Gleichstellungsstelle einer kommunalen Stadtverwaltung (Einwohner*innen ca. 74.500) und richten uns mit unserer Arbeit grundsätzlich an alle Menschen.
Wir wollen eine Broschüre zum Handlungsleitfaden für die geschlechtergerechte Sprache bei der Stadt erstellen. Dieser soll an die Beschäftigten als Unterstützung verteilt werden.
Aufgabenstellung
- Broschüre mit Wire-O-Bindung, Druckformat 14,8 cm x 14,8 cm, Endformat 15,0 x 15,0 cm
- Spiralbindung an der Kopfseite
- doppelseitiges Deckblatt und Rückseite
- 16 Seiten Inhalt, wobei lediglich die Vorderseiten Text enthalten
- Schriftart (optimal Avenir Next, alternativ Arial) und Farbschema laut Corporate Design
- Der Text ist vorgegeben, die Gestaltung ist im Rahmen des Corporate Designs frei
Es soll eine ansprechende Broschüre gestaltet werden, welche die Leser*innen zum Blättern einlädt. Das bedeutet, dass alle Seiten (Deckblatt, Inhaltsseiten und Rückseiten) bei der Gestaltung berücksichtigt werden müssen.
Am Ende soll neben den üblichen Dateien auch eine fertige Druckdatei (siehe Datenblatt) zur Verfügung gestellt werden. Dabei ist zu beachten, dass die Spiralbindung des fertigen Produkts an der Kopfseite sein soll.

```html
<!DOCTYPE html>
<html lang="de">
<head>
<meta charset="utf-8">
<title>Gleichstellungsstelle – Zitat</title>
<link rel="stylesheet" href="https://fonts.googleapis.com/css2?family=Nunito+Sans:wght@400;500;600&display=swap">
<style>
  :root {
    --page-bg: #b3c7c4;
    --quote-ink: #0e4f48;
    --logo-ink: #1a1a1a;
  }
  html, body {
    margin: 0;
    padding: 0;
    overflow: hidden;
  }
  .page {
    position: relative;
    width: 1200px;
    height: 1200px;
    background: var(--page-bg);
    font-family: "Nunito Sans", "Avenir Next", Arial, sans-serif;
    overflow: hidden;
  }
  .quote {
    position: absolute;
    top: 250px;
    left: 0;
    width: 1200px;
    margin: 0;
    text-align: center;
    color: var(--quote-ink);
    font-size: 41px;
    font-weight: 600;
    line-height: 53.5px;
    letter-spacing: 0.2px;
  }
  .quote-source {
    position: absolute;
    top: 532px;
    right: 246px;
    margin: 0;
    color: var(--quote-ink);
    font-size: 25px;
    font-weight: 500;
  }
  .office-mark {
    position: absolute;
    left: 70px;
    top: 1055px;
    height: 75px;
    display: flex;
    align-items: center;
    color: var(--logo-ink);
  }
  .office-name {
    display: flex;
    flex-direction: column;
    align-items: flex-end;
  }
  .office-city {
    font-size: 16px;
    font-weight: 400;
    line-height: 1;
    margin-bottom: 6px;
  }
  .office-title {
    font-size: 34px;
    font-weight: 400;
    line-height: 1;
  }
  .office-divider {
    width: 2px;
    height: 72px;
    background: var(--logo-ink);
    margin-left: 16px;
  }
  .city-mark {
    position: absolute;
    left: 896px;
    top: 1055px;
    color: var(--logo-ink);
  }
  .city-label {
    display: block;
    font-size: 18px;
    font-weight: 400;
    line-height: 1;
    margin-bottom: 6px;
  }
  .city-name {
    display: block;
    font-size: 40px;
    font-weight: 400;
    line-height: 1;
  }
</style>
</head>
<body>
  <main class="page">
    <blockquote class="quote">
      „Gerechte Sprache allein schafft<br>
      noch keine gerechte Welt.<br>
      Aber indem wir sie verwenden,<br>
      zeigen wir, dass wir eine gerechte<br>
      Welt überhaupt wollen“
    </blockquote>
    <p class="quote-source">(Anselm Trevisko)</p>

    <div class="office-mark">
      <div class="office-name">
        <span class="office-city">Stadt Herwangen</span>
        <span class="office-title">Gleichstellungsstelle</span>
      </div>
      <span class="office-divider"></span>
    </div>

    <div class="city-mark">
      <span class="city-label">Stadt</span>
      <span class="city-name">Herwangen</span>
    </div>
  </main>
</body>
</html>
```